Create an epic logo and package design for new hair care line!

Hello designers! I am rebranding my entire hair care company from top to bottom. I am looking for a package design that will inspire the direction of the entire brand and feel of the company moving forward.

I need the design to be epic, clear, and attention getting. You have free range when it comes to the color palette and font. Nothing is off the table, I want you to really feel like you can take this in any direction!

A little background on the company and our products.
The company is called VexOra which is also the name of our hero product. VexOra is an Ayurvedic hair growth oil infused with CBD that is also organic, vegan and cruelty free. This is the first and only ayurvedic hair growth oil on the market that contains full spectrum CBD. It seriously works to grow hair from anyone who just wants longer hair, to someone who might be balding or who has lost their hair. Very exciting!

I need you to design the logo for the brand, "VexOra" and packaging for the product for retail. I need to see what the package will look like. The package is very important. This will be sold in a rectangular box approx 3"x3"x4". Get creative!

I have several other products that I am launching for this company, and I will hire the winner to design the packaging for those products as well. This will be ongoing work!

Thank you and please reach out if you have any questions!

***Some design notes***
-If you can somehow make the "E" and the "W" in VexOra lower case or separate, that is ideal.
-Connect the word "Ora" in the word "VexOra" instead of highlighting CBD, highlight the word Ora.
-Please stay away from marijuana leaves. This is a hair care product, and I want to highlight that. I do not want to highlight the marijuana aspect.

**UPDATE** Respectfully, I will reject anything that is simply a logo on a building. I am not interested in that, I am interested in an entire design concept for this company. I am really looking to see your BRANDING CONCEPT for this company through PACKAGING. Out of almost 300 entries, only 3-4 people have actually put time into designing packaging. I say this because you have a really good chance of winning if you simply put some thought into the design of this package. Thank you thank you! I'm excited to see where this goes!

-Tobin

```html
<!DOCTYPE html>
<html lang="en">
<head>
<meta charset="utf-8">
<title>VexOra – Packaging Concept</title>
<link href="https://fonts.googleapis.com/css2?family=Montserrat:wght@400;600&family=Great+Vibes&display=swap" rel="stylesheet">
<style>
  :root {
    --bg: #ececec;
    --paper: #ffffff;
    --green-dark: #5a8a22;
    --green: #8dbb52;
    --blush: #f8dcd1;
    --peach: #f6b9a1;
    --lid-light: #f3eeec;
    --lid-mid: #e5d9d6;
  }
  * { margin: 0; padding: 0; box-sizing: border-box; }
  html, body { width: 1200px; height: 1200px; overflow: hidden; background: var(--bg); }
  .canvas { position: relative; width: 1200px; height: 1200px; }

  .brand-name { font-family: "Montserrat", sans-serif; font-weight: 600; color: var(--green-dark); line-height: 1; white-space: nowrap; }
  .tagline { font-family: "Montserrat", sans-serif; font-weight: 600; color: var(--green); letter-spacing: 0.45em; text-transform: uppercase; white-space: nowrap; }
  .subline { font-family: "Montserrat", sans-serif; font-weight: 400; color: var(--green-dark); text-transform: uppercase; letter-spacing: 0.08em; white-space: nowrap; }
  .sprig { position: absolute; background: var(--green); border-radius: 40% 60% 45% 55%; opacity: 0.85; }
  .disc { position: absolute; border-radius: 50%; }

  /* box front panel */
  .box-front { position: absolute; left: 97px; top: 550px; width: 310px; height: 323px; background: var(--paper); overflow: hidden; box-shadow: 0 2px 10px rgba(0,0,0,.08); }
  .box-front .brand-name { position: absolute; left: 0; width: 100%; text-align: center; top: 90px; font-size: 38px; }
  .box-front .tagline { position: absolute; left: 0; width: 100%; text-align: center; top: 142px; font-size: 12px; padding-left: 0.45em; }
  .box-front .subline { position: absolute; left: 0; width: 100%; text-align: center; top: 162px; font-size: 8px; }

  /* lid panel */
  .lid { position: absolute; left: 483px; top: 450px; width: 450px; height: 420px; background: linear-gradient(160deg, var(--lid-light) 0%, var(--lid-mid) 55%, var(--lid-light) 100%); box-shadow: 0 2px 10px rgba(0,0,0,.08); display: flex; align-items: center; justify-content: center; }
  .lid-message { font-family: "Great Vibes", cursive; font-size: 64px; color: var(--green-dark); }

  /* tall label */
  .label { position: absolute; left: 961px; top: 121px; width: 200px; height: 415px; background: var(--paper); overflow: hidden; box-shadow: 0 2px 10px rgba(0,0,0,.08); }
  .label .name-small { position: absolute; left: 22px; top: 22px; font-size: 16px; }
  .label .name-large { position: absolute; left: 0; width: 100%; text-align: center; top: 180px; font-size: 34px; }
  .label .tagline { position: absolute; left: 0; width: 100%; text-align: center; top: 226px; font-size: 11px; letter-spacing: 0.4em; padding-left: 0.4em; }
  .label .subline { position: absolute; left: 0; width: 100%; text-align: center; top: 244px; font-size: 7px; }
  .label .infused { position: absolute; left: 104px; top: 334px; font-family: "Montserrat", sans-serif; font-size: 8px; color: var(--green-dark); text-transform: uppercase; letter-spacing: 0.05em; white-space: nowrap; }
  .label .volume { position: absolute; left: 140px; top: 392px; font-family: "Montserrat", sans-serif; font-size: 7px; color: var(--green-dark); }

  /* bottle wrap label */
  .wrap-label { position: absolute; left: 1000px; top: 570px; width: 71px; height: 299px; background: var(--paper); overflow: hidden; box-shadow: 0 2px 10px rgba(0,0,0,.08); }
  .wrap-label .band { position: absolute; left: 0; top: 0; width: 100%; height: 70px; background: var(--blush); }
  .wrap-label .brand-name { position: absolute; left: 0; width: 100%; text-align: center; top: 188px; font-size: 13px; }
  .wrap-label .tagline { position: absolute; left: 0; width: 100%; text-align: center; top: 206px; font-size: 5px; letter-spacing: 0.25em; }
  .wrap-label .subline { position: absolute; left: 0; width: 100%; text-align: center; top: 214px; font-size: 4px; }

  /* palette + name lockups */
  .palette { position: absolute; left: 90px; top: 970px; display: flex; gap: 2px; }
  .swatch { width: 42px; height: 44px; }
  .lockup { position: absolute; top: 955px; font-size: 76px; }
  .lockup-primary { left: 325px; }
  .lockup-secondary { left: 760px; color: var(--green); }
</style>
</head>
<body>
<main class="canvas">

  <section class="box-front" aria-label="Box front panel">
    <div class="disc" style="left:-20px; top:210px; width:190px; height:190px; background: var(--blush);"></div>
    <div class="disc" style="left:240px; top:255px; width:110px; height:110px; background: var(--peach);"></div>
    <div class="sprig" role="img" aria-label="Green leaf sprig" style="left:10px; top:225px; width:80px; height:90px;"></div>
    <div class="sprig" role="img" aria-label="Green leaf sprig" style="left:210px; top:195px; width:85px; height:80px;"></div>
    <p class="brand-name">VexOra</p>
    <p class="tagline">Ayurvedic</p>
    <p class="subline">hair growth oil</p>
  </section>

  <section class="lid" role="img" aria-label="Soft silky hair texture background">
    <p class="lid-message">We Care....</p>
  </section>

  <section class="label" aria-label="Product label">
    <div class="disc" style="left:110px; top:25px; width:140px; height:140px; background: var(--green);"></div>
    <div class="disc" style="left:-55px; top:300px; width:150px; height:150px; background: var(--blush);"></div>
    <div class="sprig" role="img" aria-label="Light leaf sprig" style="left:148px; top:55px; width:42px; height:75px; background: var(--paper); opacity:.6;"></div>
    <div class="sprig" role="img" aria-label="Green leaf sprig" style="left:12px; top:290px; width:80px; height:90px;"></div>
    <p class="brand-name name-small">VexOra</p>
    <p class="brand-name name-large">VexOra</p>
    <p class="tagline">Ayurvedic</p>
    <p class="subline">hair growth oil</p>
    <p class="infused">Infused with CBD</p>
    <p class="volume">15ml</p>
  </section>

  <section class="wrap-label" aria-label="Bottle label">
    <div class="band"></div>
    <div class="disc" style="left:36px; top:110px; width:60px; height:60px; background: var(--green);"></div>
    <div class="sprig" role="img" aria-label="Green leaf sprig" style="left:6px; top:238px; width:30px; height:36px;"></div>
    <p class="brand-name">VexOra</p>
    <p class="tagline">Ayurvedic</p>
    <p class="subline">hair growth oil</p>
  </section>

  <div class="palette" aria-label="Colour palette">
    <span class="swatch" style="background: var(--green-dark);"></span>
    <span class="swatch" style="background: var(--green);"></span>
    <span class="swatch" style="background: var(--blush);"></span>
    <span class="swatch" style="background: var(--peach);"></span>
  </div>

  <p class="brand-name lockup lockup-primary">VexOra</p>
  <p class="brand-name lockup lockup-secondary">VexOra</p>

</main>
</body>
</html>
```